Upgrade 4 Images - Bid 1, then we can discuss the other 3

We have a four graphics that we use in various presentations and business proposals. We want to upgrade them to make them really pop and match the level of service we provide, without going overboard.

We're open to new ideas, but the general form and content should stay the same.

I'd like to have all four designed by the same person, but I'm assuming this bid will be for 1 of the four, and then the other three can be contracted as additions.

```html
<!DOCTYPE html>
<html lang="en">
<head>
<meta charset="utf-8">
<title>Operating Quadrants – Data Processing as a Service</title>
<link href="https://fonts.googleapis.com/css2?family=Nunito+Sans:wght@300;400;600&display=swap" rel="stylesheet">
<style>
  :root {
    --navy-deep: #17193a;
    --navy: #262c52;
    --dusk: #3b3958;
    --plum: #4a3550;
    --bar-dark: #16121f;
    --orange: #f08a3c;
    --white: #ffffff;
    --peach: #ffc3a2;
    --coral: #f27a68;
    --rose: #e25a63;
  }
  * { margin: 0; padding: 0; box-sizing: border-box; }
  html, body { width: 1200px; height: 675px; overflow: hidden; background: var(--navy-deep); }
  .slide {
    position: relative;
    width: 1200px;
    height: 675px;
    overflow: hidden;
    font-family: "Nunito Sans", sans-serif;
  }
  .scene-backdrop {
    position: absolute;
    inset: 0;
    background:
      radial-gradient(ellipse at 80% 85%, rgba(150, 70, 90, 0.45), transparent 60%),
      radial-gradient(ellipse at 55% 30%, rgba(120, 125, 165, 0.35), transparent 55%),
      linear-gradient(100deg, var(--navy-deep) 0%, var(--navy) 35%, var(--dusk) 70%, var(--plum) 100%);
  }
  .title {
    position: absolute;
    top: 40px;
    left: 0;
    width: 100%;
    text-align: center;
    color: var(--white);
    font-weight: 400;
    font-size: 50px;
    letter-spacing: 1px;
    line-height: 1;
  }
  .subtitle {
    position: absolute;
    top: 89px;
    left: 0;
    width: 100%;
    text-align: center;
    color: var(--orange);
    font-weight: 300;
    font-size: 29px;
    letter-spacing: 0.5px;
    line-height: 1;
  }
  .quadrant-diagram {
    position: absolute;
    inset: 0;
    width: 1200px;
    height: 675px;
  }
  .axis-bar { fill: var(--bar-dark); opacity: 0.92; }
  .axis-label { fill: var(--orange); font-size: 22px; font-weight: 400; }
  .quadrant-label { fill: var(--white); font-size: 38px; font-weight: 400; }
  .center-label { fill: var(--white); font-size: 31px; font-weight: 300; }
  .brand-name {
    position: absolute;
    left: 84px;
    top: 510px;
    width: 100px;
    text-align: center;
    color: var(--orange);
    font-weight: 400;
    line-height: 1;
  }
  .brand-name .brand-article { display: block; font-size: 22px; margin-bottom: 6px; }
  .brand-name .brand-word { display: block; font-size: 27px; margin-bottom: 4px; }
  .brand-name .brand-suffix { display: block; font-size: 33px; }
  .web-address {
    position: absolute;
    right: 58px;
    top: 609px;
    color: var(--white);
    font-size: 17px;
    font-weight: 300;
    letter-spacing: 1px;
  }
</style>
</head>
<body>
<div class="slide">
  <div class="scene-backdrop" role="img" aria-label="Dimmed photo of business people in silhouette seated around a meeting table, tinted deep blue and plum"></div>

  <h1 class="title">OPERATIN QUADRANTS</h1>
  <p class="subtitle">Data Processing as a Service</p>

  <svg class="quadrant-diagram" viewBox="0 0 1500 844" xmlns="http://www.w3.org/2000/svg">
    <defs>
      <linearGradient id="grad-specialist" x1="488" y1="452" x2="732" y2="208" gradientUnits="userSpaceOnUse">
        <stop offset="0" stop-color="#ffd2b4" stop-opacity="0.95"/>
        <stop offset="0.5" stop-color="#f4927c" stop-opacity="0.75"/>
        <stop offset="1" stop-color="#ffb792" stop-opacity="0.95"/>
      </linearGradient>
      <linearGradient id="grad-enterprise" x1="782" y1="208" x2="1026" y2="452" gradientUnits="userSpaceOnUse">
        <stop offset="0" stop-color="#ffc3a2" stop-opacity="0.95"/>
        <stop offset="0.55" stop-color="#f27a68" stop-opacity="0.85"/>
        <stop offset="1" stop-color="#ffb08c" stop-opacity="0.95"/>
      </linearGradient>
      <linearGradient id="grad-adhoc" x1="488" y1="510" x2="732" y2="754" gradientUnits="userSpaceOnUse">
        <stop offset="0" stop-color="#ffd0b0" stop-opacity="0.95"/>
        <stop offset="0.5" stop-color="#e86a66" stop-opacity="0.7"/>
        <stop offset="1" stop-color="#c9475a" stop-opacity="0.5"/>
      </linearGradient>
      <linearGradient id="grad-factory" x1="782" y1="754" x2="1026" y2="510" gradientUnits="userSpaceOnUse">
        <stop offset="0" stop-color="#ffb48e" stop-opacity="0.95"/>
        <stop offset="0.5" stop-color="#ef5d62" stop-opacity="0.85"/>
        <stop offset="1" stop-color="#f4907a" stop-opacity="0.7"/>
      </linearGradient>
    </defs>

    <g class="quadrant-strips">
      <polygon class="strip-specialist" fill="url(#grad-specialist)" points="712,208 732,228 732,258 538,452 506,452 488,434"/>
      <polygon class="strip-enterprise" fill="url(#grad-enterprise)" points="802,208 782,228 782,258 976,452 1008,452 1026,434"/>
      <polygon class="strip-adhoc" fill="url(#grad-adhoc)" points="712,754 732,734 732,704 538,510 506,510 488,528"/>
      <polygon class="strip-factory" fill="url(#grad-factory)" points="802,754 782,734 782,704 976,510 1008,510 1026,528"/>
    </g>

    <g class="axes">
      <polygon class="axis-bar" points="757,200 782,225 782,737 757,762 732,737 732,225"/>
      <polygon class="axis-bar" points="474,478 499,453 1009,453 1034,478 1009,503 499,503"/>
    </g>

    <g class="axis-labels">
      <text class="axis-label" transform="translate(765,310) rotate(-90)" text-anchor="middle">High Maturity</text>
      <text class="axis-label" transform="translate(750,654) rotate(90)" text-anchor="middle">Low Maturity</text>
      <text class="axis-label" x="589" y="486" text-anchor="middle">Low Utilization</text>
      <text class="axis-label" x="924" y="484" text-anchor="middle">High Utilization</text>
    </g>

    <g class="quadrant-labels">
      <text class="quadrant-label" transform="translate(622,343) rotate(-45)" text-anchor="middle">Specialist</text>
      <text class="quadrant-label" transform="translate(890,350) rotate(45)" text-anchor="middle">Enterprise</text>
      <text class="quadrant-label" transform="translate(617,630) rotate(45)" text-anchor="middle">Ad Hoc</text>
      <text class="quadrant-label" transform="translate(895,621) rotate(-45)" text-anchor="middle">Factory</text>
    </g>

    <g class="center-label-group" transform="translate(748,480) rotate(-40)">
      <text class="center-label" x="0" y="-4" text-anchor="middle">Goldilocks</text>
      <text class="center-label" x="0" y="30" text-anchor="middle">Zone</text>
    </g>
  </svg>

  <div class="brand-name">
    <span class="brand-article">The</span>
    <span class="brand-word">Corvane</span>
    <span class="brand-suffix">Group</span>
  </div>

  <div class="web-address">www.corvanegroup.com</div>
</div>
</body>
</html>
```